Package Design for New Fruit Juice product - MELLOW PIPS

Our Company a Food and Beverage provider is launching 6 fruit juice variants.
We want to create the packaging for the different products.
The product name is Mellow Pips (Logo attached) and this product is expected to be in the top category within the industry.
The startup products are
1) ORANGE JUICE
2) APPLE JUICE
3) MIXED BERRIES : apple, aronia, blackcurrant, strawberry
4) WHITE & RED GRAPE
5) CONCORD GRAPE
6) TROPICAL
There are 3 elements which we want to be incorporated into the front design.
1) a pouring effect : ie juice pouring from a source (if realistic, we want this source to be the spout of the box or you can create your own ideas)
2) a splash effect: the juice pours into a splash at the front of the box
3) the fruit(s) at the base of the box
a similar example is Solvik Juice: image attached to brief
We expect all product packages to follow similar design concept for consistency.
The colours to be used should match the respective fruits. Soft colors only, nothing too bold.
The Packaging type is the rectangular Cartomex (see attachments)
We invite creative and innovative designers to submit their designs for our project..
The deliverable is
1. Design in Keyline Design Sheet flat format
2. Design in Box format
3. For all 6 products
Kindly contact with any further information you may require in order to further understand this brief.
Finally, selected designer must commit to a 30day post project support, as design will be submitted for regulatory approval and very minor changes may be required.

```html
<!DOCTYPE html>
<html lang="en">
<head>
<meta charset="utf-8">
<title>Mellow Pips – Premium Fruit Juice Cartons</title>
<link href="https://fonts.googleapis.com/css2?family=Chewy&family=Sniglet:wght@400;800&family=Arimo:wght@400;700&display=swap" rel="stylesheet">
<style>
  :root{
    --bg:#f1f1f1;
    --carton-white:#fbfbfb;
    --leaf:#8fb04c;
    --leaf-dark:#6e9135;
    --leaf-deep:#4f7424;
    --cream:#eef2c4;
    --ink:#1b1b1b;
    --grey-text:#5b5b5b;
    --apple-1:#f6d6b8;
    --apple-2:#e8874e;
    --apple-3:#c9462f;
    --orange-1:#fde9a0;
    --orange-2:#f8c02e;
    --orange-3:#f09a12;
  }
  *{box-sizing:border-box;margin:0;padding:0}
  html,body{width:1200px;height:1000px;overflow:hidden;background:var(--bg)}
  body{position:relative;font-family:"Arimo",Arial,sans-serif}

  .carton{position:absolute;top:150px;width:440px;height:690px;display:flex;box-shadow:0 18px 30px rgba(0,0,0,.12)}
  .carton--apple{left:130px}
  .carton--orange{left:630px}

  .panel{position:relative;height:100%;background:var(--carton-white);overflow:hidden}
  .panel--front{width:300px}
  .panel--side{width:140px;border-left:1px solid #dcdcdc}

  .panel__top-strip{position:absolute;left:0;top:0;width:100%;height:28px;background:var(--leaf)}

  .pour-stream{position:absolute;top:28px;left:150px;width:90px;height:240px;border-radius:45px 45px 0 0}
  .carton--apple .pour-stream{background:linear-gradient(200deg,rgba(232,135,78,.55),rgba(246,214,184,.25))}
  .carton--orange .pour-stream{background:linear-gradient(200deg,rgba(248,192,46,.85),rgba(253,233,160,.35))}

  .brand{position:absolute;top:52px;left:24px;display:flex;align-items:center;gap:8px}
  .brand__dot{width:22px;height:22px;border-radius:50%;background:var(--leaf)}
  .brand__name{font-family:"Sniglet",sans-serif;font-weight:800;font-size:30px;line-height:.95;color:var(--ink);width:90px}

  .info-band{position:absolute;left:0;top:250px;width:100%;height:210px;background:var(--leaf);border-bottom:3px solid var(--leaf-deep)}
  .info-band__tagline{margin-top:14px;text-align:center;font-family:"Sniglet",sans-serif;font-weight:800;font-size:21px;color:var(--cream)}
  .info-band__product{margin-top:6px;text-align:center;font-family:"Chewy",sans-serif;font-size:56px;line-height:.95;color:#fff;
    -webkit-text-stroke:2.5px var(--ink);paint-order:stroke fill;letter-spacing:1px}

  .nutrition{position:absolute;left:22px;bottom:12px;width:256px;display:grid;grid-template-columns:repeat(5,1fr);gap:3px}
  .nutrition__cell{font-size:8.5px;text-align:center;line-height:1.1}
  .nutrition__label{background:var(--cream);color:var(--ink);padding:2px 0;border-radius:2px 2px 0 0}
  .nutrition__pct{background:var(--leaf-deep);color:#fff;font-weight:700;padding:1px 0;border-radius:0 0 2px 2px}

  .fruit-photo{position:absolute;left:0;top:463px;width:100%;height:227px}
  .carton--apple .fruit-photo{background:radial-gradient(ellipse at 45% 55%,var(--apple-1) 0%,var(--apple-2) 45%,var(--apple-3) 75%,#f3d9c6 100%)}
  .carton--orange .fruit-photo{background:radial-gradient(ellipse at 55% 55%,var(--orange-2) 0%,var(--orange-3) 45%,var(--orange-1) 80%,#fff6d8 100%)}

  .volume{position:absolute;left:0;right:0;bottom:28px;text-align:center;font-weight:700;font-size:22px;color:var(--ink)}
  .volume small{font-size:13px}
  .net-weight{position:absolute;left:0;right:0;bottom:12px;text-align:center;font-weight:700;font-size:9px;color:var(--ink)}

  .side-table{position:absolute;left:6px;top:262px;width:128px;border-collapse:collapse;font-size:6px;color:var(--cream)}
  .side-table td,.side-table th{border:1px solid rgba(238,242,196,.55);height:20px;text-align:center;font-weight:400}
  .side-table th{height:22px}

  .side-copy{position:absolute;left:8px;top:474px;width:124px;font-size:6.6px;line-height:1.3;color:var(--grey-text)}
  .side-copy p{margin-bottom:7px}
  .side-copy strong{color:#333}
</style>
</head>
<body>

<!-- Apple carton -->
<section class="carton carton--apple">
  <div class="panel panel--front">
    <div class="panel__top-strip"></div>
    <div class="pour-stream" role="img" aria-label="Apple juice pouring down from the carton spout"></div>
    <div class="brand"><span class="brand__dot"></span><span class="brand__name">Mellow Pips</span></div>
    <div class="info-band">
      <p class="info-band__tagline">Premium Fruit Juice</p>
      <h2 class="info-band__product">APPLE<br>JUICE</h2>
      <div class="nutrition">
        <div class="nutrition__cell"><div class="nutrition__label">Calories<br>33 kcal</div><div class="nutrition__pct">2%</div></div>
        <div class="nutrition__cell"><div class="nutrition__label">Sugars<br>7.7g</div><div class="nutrition__pct">9%</div></div>
        <div class="nutrition__cell"><div class="nutrition__label">Fat<br>0.0g</div><div class="nutrition__pct">0%</div></div>
        <div class="nutrition__cell"><div class="nutrition__label">Saturates<br>0.0g</div><div class="nutrition__pct">0%</div></div>
        <div class="nutrition__cell"><div class="nutrition__label">Salt<br>0.0g</div><div class="nutrition__pct">0%</div></div>
      </div>
    </div>
    <div class="fruit-photo" role="img" aria-label="Half an apple with a juice splash"></div>
    <p class="volume">℮1<small>L</small></p>
    <p class="net-weight">Net Wt. 30 fl.OZ</p>
  </div>
  <div class="panel panel--side">
    <div class="panel__top-strip"></div>
    <table class="side-table">
      <tr><th>energy</th><th>concentrate</th><th>energy</th><th>energy</th></tr>
      <tr><td>energy</td><td>1145</td><td>0</td><td>65</td></tr>
      <tr><td>energy</td><td>0</td><td>1145</td><td>1145</td></tr>
      <tr><td>energy</td><td>63</td><td>83</td><td>1145</td></tr>
      <tr><td>energy</td><td>0</td><td>0</td><td>65</td></tr>
      <tr><td>energy</td><td>0</td><td>1145</td><td>2</td></tr>
      <tr><td>energy</td><td>0</td><td>1145</td><td>2</td></tr>
      <tr><td>energy</td><td>0</td><td>1145</td><td>1145</td></tr>
      <tr><td>energy</td><td>0</td><td>1145</td><td>65</td></tr>
    </table>
    <div class="side-copy">
      <p>**NOTE TO DESIGNERS: use 250ml serving information only in design</p>
      <p>The trademark Mellow Pips™, Mellow Pips logo, and green explosion design are the properties of Verano Food Company Limited.</p>
      <p><strong>Ingredients (en)</strong><br>Purified water, Orange Juice, Apple Juice, Ruby Grapefruit, Lemon Juice</p>
      <p><strong>Ingrédients (fr)</strong><br>Eau purifiée, jus d'orange, jus de pomme, de pamplemousse Ruby, jus de citron</p>
      <p>NUTRITIONAL INFORMATION TABLE, USE 250ML SERVING</p>
    </div>
  </div>
</section>

<!-- Orange carton -->
<section class="carton carton--orange">
  <div class="panel panel--front">
    <div class="panel__top-strip"></div>
    <div class="pour-stream" role="img" aria-label="Orange juice pouring down from the carton spout"></div>
    <div class="brand"><span class="brand__dot"></span><span class="brand__name">Mellow Pips</span></div>
    <div class="info-band">
      <p class="info-band__tagline">Premium Fruit Juice</p>
      <h2 class="info-band__product">ORANGE<br>JUICE</h2>
      <div class="nutrition">
        <div class="nutrition__cell"><div class="nutrition__label">Calories<br>33 kcal</div><div class="nutrition__pct">2%</div></div>
        <div class="nutrition__cell"><div class="nutrition__label">Sugars<br>7.7g</div><div class="nutrition__pct">9%</div></div>
        <div class="nutrition__cell"><div class="nutrition__label">Fat<br>0.0g</div><div class="nutrition__pct">0%</div></div>
        <div class="nutrition__cell"><div class="nutrition__label">Saturates<br>0.0g</div><div class="nutrition__pct">0%</div></div>
        <div class="nutrition__cell"><div class="nutrition__label">Salt<br>0.0g</div><div class="nutrition__pct">0%</div></div>
      </div>
    </div>
    <div class="fruit-photo" role="img" aria-label="Orange wedges with a juice splash"></div>
    <p class="volume">℮1<small>L</small></p>
    <p class="net-weight">Net Wt. 30 fl.OZ</p>
  </div>
  <div class="panel panel--side">
    <div class="panel__top-strip"></div>
    <table class="side-table">
      <tr><th>energy</th><th>concentrate</th><th>energy</th><th>energy</th></tr>
      <tr><td>energy</td><td>1145</td><td>0</td><td>65</td></tr>
      <tr><td>energy</td><td>0</td><td>1145</td><td>1145</td></tr>
      <tr><td>energy</td><td>63</td><td>83</td><td>1145</td></tr>
      <tr><td>energy</td><td>0</td><td>0</td><td>65</td></tr>
      <tr><td>energy</td><td>0</td><td>1145</td><td>2</td></tr>
      <tr><td>energy</td><td>0</td><td>1145</td><td>2</td></tr>
      <tr><td>energy</td><td>0</td><td>1145</td><td>1145</td></tr>
      <tr><td>energy</td><td>0</td><td>1145</td><td>65</td></tr>
    </table>
    <div class="side-copy">
      <p>**NOTE TO DESIGNERS: use 250ml serving information only in design</p>
      <p>The trademark Mellow Pips™, Mellow Pips logo, and green explosion design are the properties of Verano Food Company Limited.</p>
      <p><strong>Ingredients (en)</strong><br>Purified water, Orange Juice, Apple Juice, Ruby Grapefruit, Lemon Juice</p>
      <p><strong>Ingrédients (fr)</strong><br>Eau purifiée, jus d'orange, jus de pomme, de pamplemousse Ruby, jus de citron</p>
      <p>NUTRITIONAL INFORMATION TABLE, USE 250ML SERVING</p>
    </div>
  </div>
</section>

</body>
</html>
```